Velmoro Crafts

I would like to have a more comprehensive e-commerce website.

Please use my current website as reference and its content: https://velmorocrafts.com/.

Please code the website. I'd like to have e-commerce functionalities.

```html
<!DOCTYPE html>
<html lang="en">
<head>
<meta charset="utf-8">
<title>Velmoro Crafts</title>
<link rel="stylesheet" href="https://fonts.googleapis.com/css2?family=Alike&family=Poppins:wght@400;500;600&display=swap">
<style>
:root{
  --teal:#7bbfc4;
  --ink:#1d2b3a;
  --red:#f04b4b;
  --cream:#f7f3ee;
  --white:#ffffff;
  --muted:#4a4f57;
  --track:#eef0f1;
  --star:#f5b800;
}
*{box-sizing:border-box;margin:0;padding:0}
html,body{width:1200px;height:3604px;overflow:hidden}
body{position:relative;background:var(--white);font-family:"Poppins",sans-serif;color:var(--ink)}
.abs{position:absolute}
.serif{font-family:"Alike",serif;font-weight:400}

.topbar{left:0;top:0;width:1200px;height:34px;background:var(--teal);color:var(--white);font-size:12px;font-weight:500;text-align:center;line-height:34px;letter-spacing:.2px}
.header{left:0;top:34px;width:1200px;height:107px;background:var(--white)}
.nav{left:89px;top:48px;display:flex;gap:33px;font-size:12px;font-weight:500;color:var(--muted)}
.brand{left:450px;top:14px;width:300px;text-align:center}
.brand .dot{display:block;width:46px;height:46px;border-radius:50%;background:var(--red);margin:0 auto 8px}
.brand .name{font-family:"Alike",serif;font-size:15px;color:var(--ink);letter-spacing:1px;text-transform:uppercase}
.icons{left:960px;top:40px;display:flex;gap:26px}
.icons svg{width:30px;height:30px}

.hero{left:0;top:141px;width:1200px;height:600px;background:linear-gradient(100deg,#ecebea 0%,#e6e3df 40%,#cdbca6 62%,#8a5a35 80%,#5a3a24 100%)}
.hero-title{left:89px;top:252px;font-size:60px;line-height:66px;color:var(--ink)}
.hero-text{left:89px;top:404px;width:450px;font-size:12.5px;line-height:22.5px;color:#3a3f46}
.btn{background:var(--red);color:var(--white);font-size:13px;font-weight:500;text-transform:uppercase;display:flex;align-items:center;justify-content:center}
.hero-btn{left:89px;top:513px;width:326px;height:42px}

.section-title{font-size:42px;color:var(--ink)}
.products-title{left:88px;top:822px}
.view-all{right:89px;top:836px;font-size:13px;color:var(--red);border-bottom:1px solid var(--red);padding-bottom:1px}
.product{top:899px;width:290px}
.product .ph{width:290px;height:336px}
.product .cap{margin-top:14px;font-size:25px;white-space:nowrap}
.track{left:89px;width:1111px;height:6px;background:var(--track);border-radius:3px}
.track .bar{width:188px;height:6px;background:var(--teal);border-radius:3px}

.about-panel{left:372px;top:1436px;width:828px;height:502px;background:var(--cream)}
.arch-frame{border:1.5px solid var(--ink);border-radius:210px 210px 0 0}
.arch-photo{border-radius:206px 206px 0 0}
.about-title{left:629px;top:1514px;font-size:42px;line-height:53px}
.about-text{left:629px;top:1636px;width:420px;font-size:12.5px;line-height:22.3px;color:#3a3f46}
.about-btn{left:629px;top:1812px;width:135px;height:43px}

.testi-title{left:0;top:2016px;width:1200px;text-align:center}
.testi{top:2115px;width:305px;height:305px;background:var(--cream);text-align:center}
.testi .q{position:absolute;left:127px;top:-14px;width:52px;height:52px;border-radius:50%;background:var(--white);color:var(--red);font-family:"Alike",serif;font-size:44px;line-height:58px}
.testi .stars{position:absolute;left:0;top:46px;width:305px;color:var(--star);font-size:21px;letter-spacing:4px}
.testi .txt{position:absolute;left:22px;top:80px;width:261px;font-size:13px;line-height:26.7px;color:#3a3f46}
.testi .av{position:absolute;left:128px;top:221px;width:50px;height:50px;border-radius:50%;background:radial-gradient(circle at 50% 55%,#f4efe7 0 40%,#b99878 70%)}
.testi .who{position:absolute;left:0;top:274px;width:305px;font-family:"Alike",serif;font-size:16px}

.contact-panel{left:0;top:2580px;width:825px;height:550px;background:var(--cream)}
.contact-title{left:89px;top:2628px;font-size:42px;line-height:54px}
.contact-sub{left:89px;top:2753px;font-size:12px;color:#3a3f46}
.field{left:89px;width:480px;background:var(--white);font-family:"Alike",serif;font-size:16px;color:#666;padding:10px 23px}
.send-btn{left:89px;top:3042px;width:135px;height:42px}

.footer{left:0;top:3221px;width:1200px;height:383px;background:var(--teal);color:var(--white)}
.vline{top:3260px;width:1px;height:283px;background:rgba(255,255,255,.7)}
.f-title{font-size:34px;color:var(--white)}
.f-links{left:143px;top:3340px;font-size:14px;line-height:26.5px;color:var(--white)}
.f-brand{left:440px;top:3262px;width:320px;text-align:center}
.f-brand .dot{display:block;width:80px;height:80px;border-radius:50%;background:var(--red);margin:0 auto 16px}
.f-brand .name{font-family:"Alike",serif;font-size:22px;color:var(--ink);letter-spacing:1.5px;text-transform:uppercase}
.social{top:3417px;width:48px;height:48px;border-radius:50%;background:#5d9ca2}
.social.first{background:var(--red)}
.c-item{left:839px;font-size:12.5px;line-height:18px;padding-left:24px;color:var(--white)}
.c-item svg{position:absolute;left:0;top:3px;width:14px;height:14px}
.f-rule{left:89px;top:3545px;width:1024px;height:1px;background:rgba(255,255,255,.7)}
.copy{left:0;top:3563px;width:1200px;text-align:center;font-size:13.5px;font-weight:500;color:var(--white)}
.to-top{left:1132px;top:3525px;width:40px;height:40px;border-radius:50%;background:var(--red);display:flex;align-items:center;justify-content:center}
</style>
</head>
<body>

<div class="abs topbar">WE LOOK FORWARD TO HEARING FROM YOU!</div>

<header class="abs header">
  <nav class="abs nav"><span>HOME</span><span>ABOUT US</span><span>PRODUCTS</span><span>CONTACT US</span></nav>
  <div class="abs brand"><span class="dot"></span><span class="name">Velmoro Crafts</span></div>
  <div class="abs icons">
    <svg viewBox="0 0 30 30" fill="none" stroke="#1d2b3a" stroke-width="2"><circle cx="15" cy="10" r="6"/><path d="M5 27c1-6 5-9 10-9s9 3 10 9"/></svg>
    <svg viewBox="0 0 30 30" fill="none" stroke="#1d2b3a" stroke-width="2"><circle cx="13" cy="13" r="8"/><path d="M19 19l7 7"/></svg>
    <svg viewBox="0 0 30 30" fill="none" stroke="#1d2b3a" stroke-width="2"><path d="M6 10h18l-1 17H7z"/><path d="M11 10V7a4 4 0 0 1 8 0v3"/><circle cx="25" cy="5" r="5" fill="#f04b4b" stroke="none"/><text x="25" y="8" font-size="8" fill="#fff" stroke="none" text-anchor="middle" font-family="Poppins,sans-serif">2</text></svg>
  </div>
</header>

<section class="abs hero" role="img" aria-label="Photo of lit amber candles, a reed diffuser and a rolled white towel on a wooden shelf"></section>
<h1 class="abs hero-title serif">Welcome to<br>Velmoro Crafts!</h1>
<p class="abs hero-text">We are a family-owned business passionate about creating beautiful, eco-friendly candles that capture the essence of the Southwest. Our candles are handcrafted by Mexican-American women who pour their love and creativity into each piece.</p>
<div class="abs btn hero-btn">Discover our handcrafted candles</div>

<h2 class="abs section-title serif products-title">Our Products</h2>
<div class="abs view-all">VIEW ALL PRODUCTS</div>
<div class="abs product" style="left:89px"><div class="ph" role="img" aria-label="Photo of a round textured concrete candle on rocks" style="background:linear-gradient(160deg,#8f7a66,#c9c4bd 50%,#7a6452)"></div><div class="cap serif">Sola Collection - $7</div></div>
<div class="abs product" style="left:402px"><div class="ph" role="img" aria-label="Photo of an oval candle with succulent decoration among green leaves" style="background:linear-gradient(160deg,#4f6b33,#7c9a4d 50%,#6d5a55)"></div><div class="cap serif">Mesa Collection - 10$</div></div>
<div class="abs product" style="left:715px"><div class="ph" role="img" aria-label="Photo of a lidded concrete candle jar on a wooden ledge" style="background:linear-gradient(160deg,#5a3b2a,#9a8a7a 50%,#6a4a3e)"></div><div class="cap serif">Cove Collection - 35$</div></div>
<div class="abs product" style="left:1028px"><div class="ph" role="img" aria-label="Photo of a candle in a glass cup styled like hot cocoa" style="background:linear-gradient(160deg,#eeeeee,#c9c6c3 50%,#8a5f48)"></div><div class="cap serif">New Collection - $</div></div>
<div class="abs track" style="top:1316px"><div class="bar"></div></div>

<div class="abs about-panel"></div>
<div class="abs arch-frame" style="left:155px;top:1438px;width:413px;height:477px"></div>
<div class="abs arch-photo" role="img" aria-label="Photo of concrete candles topped with colourful wax succulents and handmade tags" style="left:164px;top:1427px;width:411px;height:479px;background:linear-gradient(170deg,#3a3a3d,#cfc9bf 45%,#9a6ac0 60%,#2f2f31)"></div>
<h2 class="abs about-title serif">About<br>Velmoro Crafts</h2>
<p class="abs about-text">Velmoro Crafts is a Hispanic woman-owned business that began with a simple dream. Co-founder Marisol Vega, captivated by the art of crafting, started creating candles as gifts for loved ones. Inspired to minimize waste, Marisol envisioned eco-friendly con-tainers that could be repurposed after the candle burned. This passion project took root in her backyard, where she designed and crafted the very first Velmoro candles.</p>
<div class="abs btn about-btn">Learn more</div>

<h2 class="abs section-title serif testi-title">What Our Client Says</h2>
<div class="abs testi" style="left:123px"><div class="q">&ldquo;</div><div class="stars">★★★★★</div><p class="txt">Lorem ipsum dolor sit amet, consectetur adipiscing elit, sed do eiusmod tempor incididunt ut labore et dolore magna aliqua. Quis ipsum suspendisse ultrices gravida.</p><div class="av" role="img" aria-label="Client photo"></div><div class="who">Lena Hart</div></div>
<div class="abs testi" style="left:451px"><div class="q">&ldquo;</div><div class="stars">★★★★★</div><p class="txt">Lorem ipsum dolor sit amet, consectetur adipiscing elit, sed do eiusmod tempor incididunt ut labore et dolore magna aliqua. Quis ipsum suspendisse ultrices gravida.</p><div class="av" role="img" aria-label="Client photo"></div><div class="who">Lena Hart</div></div>
<div class="abs testi" style="left:779px"><div class="q">&ldquo;</div><div class="stars">★★★★★</div><p class="txt">Lorem ipsum dolor sit amet, consectetur adipiscing elit, sed do eiusmod tempor incididunt ut labore et dolore magna aliqua. Quis ipsum suspendisse ultrices gravida.</p><div class="av" role="img" aria-label="Client photo"></div><div class="who">Lena Hart</div></div>
<div class="abs testi" style="left:1107px"><div class="q">&ldquo;</div><div class="stars">★★★★★</div><p class="txt">Lorem ipsum dolor sit amet, consectetur adipiscing elit, sed do eiusmod tempor incididunt ut labore et dolore magna aliqua. Quis ipsum suspendisse ultrices gravida.</p><div class="av" role="img" aria-label="Client photo"></div><div class="who">Lena Hart</div></div>
<div class="abs track" style="top:2466px"><div class="bar"></div></div>

<div class="abs contact-panel"></div>
<h2 class="abs contact-title serif">Have questions or want to<br>place a custom order?</h2>
<p class="abs contact-sub">We're here to help! Feel free to reach out to us using the information below:</p>
<div class="abs field" style="top:2794px;height:45px">Name *</div>
<div class="abs field" style="top:2846px;height:45px">Email *</div>
<div class="abs field" style="top:2897px;height:45px">Phone *</div>
<div class="abs field" style="top:2948px;height:83px">Send Your Message *</div>
<div class="abs btn send-btn">Send now</div>
<div class="abs arch-frame" style="left:664px;top:2580px;width:445px;height:517px;border-radius:225px 225px 0 0"></div>
<div class="abs arch-photo" role="img" aria-label="Photo of an amber scented candle jar among baby's breath flowers on a knit blanket" style="left:656px;top:2571px;width:445px;height:517px;border-radius:222px 222px 0 0;background:linear-gradient(175deg,#9ca293,#d8d6cf 40%,#8a4d2a 70%,#e9e6e0)"></div>

<footer class="abs footer"></footer>
<div class="abs vline" style="left:421px"></div>
<div class="abs vline" style="left:778px"></div>
<h3 class="abs f-title serif" style="left:142px;top:3283px">Quick Link</h3>
<div class="abs f-links">Home<br>About Us<br>Products<br>Contact Us</div>
<div class="abs f-brand"><span class="dot"></span><span class="name">Velmoro Crafts</span></div>
<div class="abs social first" style="left:497px" role="img" aria-label="Social link"></div>
<div class="abs social" style="left:550px" role="img" aria-label="Social link"></div>
<div class="abs social" style="left:603px" role="img" aria-label="Social link"></div>
<div class="abs social" style="left:654px" role="img" aria-label="Social link"></div>
<h3 class="abs f-title serif" style="left:839px;top:3283px">Contact Us</h3>
<div class="abs c-item" style="top:3341px"><svg viewBox="0 0 14 14"><path d="M3 1l2 3-1.3 1.4a8 8 0 0 0 4.9 4.9L10 9l3 2-1 2.5C6 13 1 8 .5 2z" fill="#f04b4b"/></svg>Phone<br>000-000-0000</div>
<div class="abs c-item" style="top:3393px"><svg viewBox="0 0 14 14"><rect x="1" y="3" width="12" height="9" fill="#f04b4b"/><path d="M1 3l6 5 6-5" stroke="#fff" fill="none"/></svg>Email<br>velmorocrafts@gmail.com</div>
<div class="abs c-item" style="top:3444px"><svg viewBox="0 0 14 14"><path d="M7 1a4.5 4.5 0 0 1 4.5 4.5C11.5 9 7 13 7 13S2.5 9 2.5 5.5A4.5 4.5 0 0 1 7 1z" fill="#f04b4b"/><circle cx="7" cy="5.5" r="1.6" fill="#fff"/></svg>Location<br>Some Address line here<br>united kingdom CV10 4RT</div>
<div class="abs f-rule"></div>
<div class="abs copy">Copyright © 2024 All Rights Reserved</div>
<div class="abs to-top"><svg width="12" height="12" viewBox="0 0 12 12"><path d="M3 8l3-3 3 3" stroke="#fff" stroke-width="1.6" fill="none"/></svg></div>

</body>
</html>
```